Sole trader requires buisness card / company logo for mining and aviation

I require a business card and logo design having the following requirements;
Kestrel Airframe and Plant Services
Owner: Martin Hollis
Ph: 0491570156
E: martin-r-hollis@brolgamail.com.au

Logo should include a basic aircraft image and an image of an item of mining machinery either a dump truck or large excavator, but keeping in mind that the image is to be transferred onto clothing embroidery.

```html
<!DOCTYPE html>
<html lang="en">
<head>
<meta charset="utf-8">
<title>Kestrel Airframe and Plant Services – Logo and Business Card</title>
<link rel="stylesheet" href="https://fonts.googleapis.com/css2?family=Open+Sans:wght@400;600;700;800&display=swap">
<style>
  :root {
    --brand-blue: #0a72c4;
    --name-blue: #1a6fc0;
    --ink: #3a3b3d;
    --text-grey: #4a4a4a;
    --rule-grey: #d6d6d6;
    --canvas: #ffffff;
    --deco-light: #e4edf6;
    --deco-mid: #c9dbee;
  }
  html, body {
    margin: 0;
    padding: 0;
    width: 1200px;
    height: 900px;
    overflow: hidden;
    background: var(--canvas);
    font-family: "Open Sans", Arial, sans-serif;
  }
  .board {
    position: relative;
    width: 1200px;
    height: 900px;
  }
  .logo {
    position: absolute;
    display: flex;
    align-items: center;
  }
  .logo-dot {
    flex: none;
    border-radius: 50%;
    background: var(--brand-blue);
  }
  .logo-name {
    color: var(--ink);
    font-weight: 800;
    line-height: 1.05;
    letter-spacing: 0.01em;
  }
  .logo--primary {
    left: 172px;
    top: 412px;
    width: 330px;
    height: 92px;
    gap: 18px;
  }
  .logo--primary .logo-dot {
    width: 84px;
    height: 84px;
  }
  .logo--primary .logo-name {
    font-size: 24px;
  }
  .card {
    position: absolute;
    left: 570px;
    top: 324px;
    width: 464px;
    height: 269px;
    background: var(--canvas);
    border: 1px solid #e6e6e6;
    overflow: hidden;
  }
  .card-decoration {
    position: absolute;
    left: 176px;
    top: 60px;
    width: 288px;
    height: 191px;
    background: radial-gradient(ellipse at 70% 45%, var(--deco-mid) 0%, var(--deco-light) 55%, rgba(255,255,255,0) 85%);
  }
  .logo--card {
    left: 44px;
    top: 32px;
    width: 200px;
    gap: 9px;
  }
  .logo--card .logo-dot {
    width: 46px;
    height: 46px;
  }
  .logo--card .logo-name {
    font-size: 13px;
  }
  .card-holder {
    position: absolute;
    left: 43px;
    top: 134px;
    margin: 0;
    padding-bottom: 6px;
    width: 112px;
    border-bottom: 1px solid var(--rule-grey);
    color: var(--name-blue);
    font-size: 18px;
    font-weight: 700;
    white-space: nowrap;
  }
  .card-contact {
    position: absolute;
    left: 43px;
    top: 170px;
    margin: 0;
    padding: 0;
    list-style: none;
    color: var(--text-grey);
    font-size: 11px;
    line-height: 22px;
  }
  .card-band {
    position: absolute;
    left: 0;
    bottom: 0;
    width: 100%;
    height: 18px;
    background: var(--brand-blue);
  }
  .board-band {
    position: absolute;
    left: 0;
    bottom: 0;
    width: 1200px;
    height: 22px;
    background: var(--brand-blue);
  }
</style>
</head>
<body>
<main class="board">
  <div class="logo logo--primary">
    <span class="logo-dot"></span>
    <span class="logo-name">Kestrel Airframe<br>and Plant Services</span>
  </div>

  <section class="card" aria-label="Business card">
    <div class="card-decoration" role="img" aria-label="Faint enlarged brand emblem in pale blue and grey"></div>
    <div class="logo logo--card">
      <span class="logo-dot"></span>
      <span class="logo-name">Kestrel Airframe<br>and Plant Services</span>
    </div>
    <h1 class="card-holder">Martin Hollis</h1>
    <ul class="card-contact">
      <li>Ph: 0491570156</li>
      <li>E: martin-r-hollis@brolgamail.com.au</li>
    </ul>
    <div class="card-band"></div>
  </section>

  <div class="board-band"></div>
</main>
</body>
</html>
```